Pediatric Dental Practice needs a postcard for direct mail advertising

We are looking for a creative and professional double-sided postcard design for a direct mail marketing campaign. Our goal is to attract new families to our pediatric dental practice by conveying a sense of warmth, modern care, and clinical excellence. The design should feel "boutique" and high-end yet remain fun and approachable for parents and children.

```html
<!DOCTYPE html>
<html lang="en">
<head>
<meta charset="utf-8">
<title>Maple Grove Pediatric Dentistry – Postcard</title>
<link rel="stylesheet" href="https://fonts.googleapis.com/css2?family=Poppins:wght@400;500;600;700&family=Hind:wght@300;400;700&family=Great+Vibes&display=swap">
<style>
  :root {
    --board: #232323;
    --cream: #faf9f4;
    --green: #26a05c;
    --green-light: #5cbf7a;
    --green-pale: #a9dbb6;
    --ink: #1c1c1c;
    --white: #ffffff;
  }
  * { margin: 0; padding: 0; box-sizing: border-box; }
  html, body { width: 994px; height: 1200px; overflow: hidden; background: var(--board); }
  .board { position: relative; width: 994px; height: 1200px; background: var(--board); }
  .card { position: absolute; left: 139px; width: 717px; overflow: hidden; background: var(--cream); }
  .card--front { top: 97px; height: 488px; }
  .card--back { top: 616px; height: 487px; }
  .card svg.art { position: absolute; inset: 0; width: 100%; height: 100%; }

  .brand { position: absolute; left: 0; width: 310px; text-align: center; font-family: "Poppins", sans-serif; color: #333; }
  .brand__mark { position: absolute; left: 126px; top: 22px; width: 58px; height: 58px; border-radius: 50%; background: var(--green-pale); }
  .brand__name { position: absolute; top: 94px; width: 100%; font-size: 38px; font-weight: 500; letter-spacing: 1px; }
  .brand__sub { position: absolute; top: 152px; width: 100%; font-size: 12px; font-weight: 500; letter-spacing: 4.5px; }

  .headline { position: absolute; left: 15px; top: 184px; width: 298px; height: 96px; color: var(--white); font-family: "Hind", sans-serif; font-weight: 400; text-align: center; }
  .headline__rule { position: absolute; left: 0; width: 100%; display: flex; align-items: center; gap: 9px; font-size: 28px; font-weight: 300; line-height: 30px; white-space: nowrap; }
  .headline__rule::before, .headline__rule::after { content: ""; flex: 1; height: 1.5px; background: var(--white); }
  .headline__rule--top { top: 2px; }
  .headline__rule--end { top: 64px; padding: 0 2px; }
  .headline__main { position: absolute; left: 0; top: 29px; width: 100%; display: block; font-size: 39px; font-weight: 700; letter-spacing: -1.8px; line-height: 36px; white-space: nowrap; }
  .promises { position: absolute; left: 0; top: 286px; width: 300px; text-align: center; color: var(--white); font-family: "Poppins", sans-serif; font-size: 17px; line-height: 21.5px; }
  .signoff { position: absolute; left: 30px; top: 410px; width: 220px; text-align: center; color: var(--white); font-family: "Great Vibes", cursive; font-size: 27px; line-height: 26px; }

  .badge { position: absolute; left: 543px; top: 330px; width: 140px; text-align: center; color: var(--green); font-family: "Poppins", sans-serif; font-weight: 700; font-size: 17.5px; line-height: 18px; }
  .badge svg { width: 26px; height: 24px; display: block; margin: 0 auto 4px; }

  .intro { position: absolute; left: 31px; top: 40px; width: 325px; font-family: "Poppins", sans-serif; font-size: 13.8px; line-height: 17px; color: var(--ink); }
  .features { position: absolute; left: 31px; top: 146px; width: 330px; list-style: none; }
  .feature { position: relative; height: 72px; padding-left: 50px; font-family: "Poppins", sans-serif; }
  .feature__icon { position: absolute; left: 0; top: 6px; width: 38px; height: 38px; border-radius: 50%; background: var(--green); display: flex; align-items: center; justify-content: center; }
  .feature__icon svg { width: 22px; height: 22px; fill: var(--white); }
  .feature__title { font-size: 15px; font-weight: 700; color: var(--green); line-height: 15px; }
  .feature__text { font-size: 14.5px; color: var(--ink); line-height: 14.5px; }

  .divider { position: absolute; left: 369px; top: 33px; width: 1.5px; height: 378px; background: var(--green); }
  .stamp { position: absolute; left: 573px; top: 29px; width: 115px; height: 115px; background: var(--green); }
  .address-line { position: absolute; left: 408px; width: 280px; height: 1px; background: var(--green); }

  .contact { position: absolute; left: 34px; top: 414px; font-family: "Poppins", sans-serif; font-size: 13px; font-weight: 500; line-height: 16px; color: var(--white); }
</style>
</head>
<body>
<div class="board">

  <section class="card card--front">
    <svg class="art" viewBox="0 0 717 488" preserveAspectRatio="none">
      <defs>
        <linearGradient id="portraitTone" x1="0" y1="0" x2="1" y2="0">
          <stop offset="0" stop-color="#9b6f52"/>
          <stop offset="0.5" stop-color="#d9b19a"/>
          <stop offset="1" stop-color="#b88a72"/>
        </linearGradient>
      </defs>
      <rect width="717" height="488" fill="var(--cream)"/>
      <path d="M0 166 C150 188 300 172 420 148 C520 128 610 112 717 120 L717 488 L0 488 Z" fill="var(--green)"/>
      <path d="M284 128 C400 98 560 80 717 88 L717 98 C560 92 420 105 284 128 Z" fill="var(--green)"/>
      <path role="img" aria-label="Photo of a smiling young girl resting her chin in her hands" d="M300 300 C320 220 360 150 430 112 C470 92 510 86 540 92 C580 100 620 150 650 230 C670 300 690 360 700 400 L300 440 Z" fill="url(#portraitTone)" opacity="0.85"/>
      <path d="M0 392 C100 370 210 380 310 420 C410 455 520 445 717 382 L717 488 L0 488 Z" fill="var(--green-light)"/>
      <path d="M0 372 C100 345 220 358 320 402 C420 440 560 440 717 372" fill="none" stroke="var(--white)" stroke-width="9"/>
      <circle cx="613" cy="396" r="79" fill="var(--white)"/>
      <circle cx="613" cy="396" r="75" fill="none" stroke="var(--green-light)" stroke-width="2"/>
    </svg>

    <div class="brand">
      <div class="brand__mark"></div>
      <div class="brand__name">maple grove</div>
      <div class="brand__sub">PEDIATRIC DENTISTRY</div>
    </div>

    <h1 class="headline">
      <span class="headline__rule headline__rule--top">GROWING</span>
      <span class="headline__main">HEALTHY SMILES</span>
      <span class="headline__rule headline__rule--end">FOR LIFE</span>
    </h1>

    <p class="promises">Compassionate care.<br>Modern technology.<br>Happy kids</p>
    <p class="signoff">Because every smile<br>has a story.</p>

    <div class="badge">
      <svg viewBox="0 0 24 22"><path fill="#26a05c" d="M12 21 C5 15 0 11 0 6 A6 6 0 0 1 12 4 A6 6 0 0 1 24 6 C24 11 19 15 12 21 Z"/></svg>
      NOW<br>WELCOMING<br>NEW<br>PATIENTS
    </div>
  </section>

  <section class="card card--back">
    <svg class="art" viewBox="0 0 717 487" preserveAspectRatio="none">
      <defs>
        <linearGradient id="officeTone" x1="0" y1="0" x2="1" y2="0">
          <stop offset="0" stop-color="#efe9df"/>
          <stop offset="0.5" stop-color="#f7f5ef"/>
          <stop offset="1" stop-color="#fbfaf6"/>
        </linearGradient>
      </defs>
      <rect role="img" aria-label="Soft faded photo of a bright dental office" width="717" height="487" fill="url(#officeTone)"/>
      <path d="M0 387 C60 373 130 375 210 397 C310 424 420 440 717 392 L717 487 L0 487 Z" fill="var(--green)"/>
    </svg>

    <p class="intro">At Maple Grove Pediatric Dentistry, we create positive dental experiences that help children build confidence and healthy habits- from their very first visit and beyond.</p>

    <ul class="features">
      <li class="feature">
        <span class="feature__icon"><svg viewBox="0 0 24 22"><path d="M12 21 C5 15 0 11 0 6 A6 6 0 0 1 12 4 A6 6 0 0 1 24 6 C24 11 19 15 12 21 Z"/></svg></span>
        <div class="feature__title">Kid-Focused Care</div>
        <div class="feature__text">Specialized pediatric training with a gentle, playful approach.</div>
      </li>
      <li class="feature">
        <span class="feature__icon"><svg viewBox="0 0 24 24"><path d="M6 2 C2 2 1 6 2 10 C3 13 4 15 5 22 L8 22 L10 15 L14 15 L16 22 L19 22 C20 15 21 13 22 10 C23 6 22 2 18 2 C15 2 14 4 12 4 C10 4 9 2 6 2 Z"/></svg></span>
        <div class="feature__title">Modern &amp; Comfortable</div>
        <div class="feature__text">State-of-the-art technology in a calming, kid-friendly environment.</div>
      </li>
      <li class="feature">
        <span class="feature__icon"><svg viewBox="0 0 24 24"><circle cx="6" cy="7" r="2.5"/><circle cx="18" cy="7" r="2.5"/><circle cx="12" cy="11" r="2"/><rect x="3" y="10.5" width="6" height="9" rx="2"/><rect x="15" y="10.5" width="6" height="9" rx="2"/><rect x="9.8" y="14" width="4.4" height="6" rx="1.5"/></svg></span>
        <div class="feature__title">Family-Centered</div>
        <div class="feature__text">We partner with parents to support lifelong oral health.</div>
      </li>
    </ul>

    <div class="divider"></div>
    <div class="stamp"></div>
    <div class="address-line" style="top:211px"></div>
    <div class="address-line" style="top:264px"></div>
    <div class="address-line" style="top:315px"></div>
    <div class="address-line" style="top:365px"></div>

    <p class="contact">BOOK TODAY!<br>(555) 014-2290 | maplegrovekids.example<br>48 Orchard Bend, Suite 200 | Fernvale, WA 98000</p>
  </section>

</div>
</body>
</html>
```